Packaging Design for Private Brand

We are re-branding all of our "private label" products. The products come in a multitude of packaging. I am looking for a clean, modern design that I will be able to apply to multiple packaging options. The first priority is a printed box that comes in a few different sizes. I'll attach the template of one of the sizes. Another is a label for a 1 gal jug. A third application is a label that can be adapted to multiple boxes and bottles.

We have a new, updated logo already (thank you Artisan Hive) and of course, we want that to be a big part of the branding. We are also looking to incorporate a way to categorize the content based on purpose (each jug with the same but in addition to the name, some sort of differentiation such as a different color arc or swoop across the bottle to indicate purpose so, maybe a general purpose cleaner will have a light blue swoop, glass cleaner a darker blue swoop, disenfectant, a red swoop, and so on. The colors don't matter now, I can grow the family as we add products, but the design needs to be adaptable.

The picture of the can is our old branding. So is the plastic jug. Looking for something better.

The box template with "Lumm" is the manufacturer's design, I've included theirs as well as the template with dimensions.

Our PMS is Reflex Blue.
Updates

Project Deadline Extended Reason: I am extending the deadline by 5 days. American holiday, Labor Day, removed me from the project for 4 days. I assumed 5 days meant five business days. Added Tuesday, September 6, 2016

Target Market(s)

Janitorial Cleaners, school janitors, kitchen workers, maintenance workers, etc.

Contact Information for Business Card

See attached current card

Font styles to use
Sans Serif

Requirements
Must have
• Logo
• For Business Card, Vornex's proven process on the back http://www.vornexsupply.example/pages/ProvenProcess/ but also enough white space to accommodate a note or jot down an appt. date.
Nice to have
• See attachment gal.jug2. What I like about this design is that the color swoop that separates the product from the branding can have different colors to denote type. EX. The yellow swoop would represent all of our degreacers. If the product inside the bottle was a general purpose cleaner, it may have a green swoop.

```html
<!DOCTYPE html>
<html lang="en">
<head>
<meta charset="utf-8">
<title>Vornex Private Label Box – Dieline</title>
<link rel="stylesheet" href="https://fonts.googleapis.com/css2?family=Montserrat:wght@600;700&family=Open+Sans:wght@400&display=swap">
<style>
  :root {
    --reflex-blue: #0057a8;
    --deep-blue: #003f98;
    --gradient-top: #1a62ad;
    --navy: #0c2b4b;
    --headline: #12325c;
    --paper: #ffffff;
    --fold-line: #e9b8c4;
    --cut-line: #c9d3df;
    --body-text: #1d2a3a;
  }
  html, body {
    margin: 0;
    padding: 0;
    width: 1200px;
    height: 421px;
    overflow: hidden;
    background: var(--paper);
  }
  .dieline {
    display: block;
    width: 1200px;
    height: 421px;
  }
  .band { fill: var(--reflex-blue); }
  .badge-dark { fill: var(--navy); }
  .panel-edge { fill: none; stroke: var(--cut-line); stroke-width: 0.8; }
  .fold { stroke: var(--fold-line); stroke-width: 0.6; stroke-dasharray: 2 2; }
  .brand-name {
    font-family: "Montserrat", sans-serif;
    font-weight: 700;
    letter-spacing: -0.3px;
  }
  .brand-name--light { fill: var(--paper); }
  .brand-name--blue { fill: var(--reflex-blue); }
  .tagline {
    font-family: "Montserrat", sans-serif;
    font-weight: 600;
    letter-spacing: -0.1px;
  }
  .tagline--light { fill: var(--paper); }
  .tagline--blue { fill: var(--reflex-blue); }
  .headline {
    font-family: "Montserrat", sans-serif;
    font-weight: 700;
    font-size: 15.5px;
    letter-spacing: 0.6px;
    fill: var(--headline);
  }
  .body-copy {
    font-family: "Open Sans", sans-serif;
    font-size: 5.2px;
    fill: var(--body-text);
  }
</style>
</head>
<body>
<svg class="dieline" viewBox="0 0 1200 421" xmlns="http://www.w3.org/2000/svg" aria-label="Vornex private label box dieline">
  <defs>
    <linearGradient id="pentagon-fill" x1="0" y1="0" x2="0" y2="1">
      <stop offset="0" stop-color="var(--gradient-top)"/>
      <stop offset="1" stop-color="var(--deep-blue)"/>
    </linearGradient>
  </defs>

  <!-- Panel outlines and folds -->
  <g class="panels">
    <rect class="panel-edge" x="402" y="72" width="196" height="280"/>
    <rect class="panel-edge" x="601" y="66" width="323" height="286"/>
    <rect class="panel-edge" x="926" y="100" width="194" height="252"/>
    <path class="panel-edge" d="M1124 138 L1148 142 L1148 284 L1124 288 Z"/>
    <line class="fold" x1="232" y1="170" x2="1148" y2="170"/>
    <line class="fold" x1="232" y1="254" x2="1148" y2="254"/>
    <line class="fold" x1="402" y1="72" x2="402" y2="352"/>
    <line class="fold" x1="924" y1="100" x2="924" y2="352"/>
  </g>

  <!-- Left end: bands and pentagon -->
  <polygon class="band" points="80,70 400,70 232,178 80,168"/>
  <polygon class="band" points="232,338 598,312 598,352 232,352"/>
  <polygon points="76,168 234,178 272,330 140,414 18,314" fill="url(#pentagon-fill)"/>
  <g class="lockup" text-anchor="end">
    <text class="brand-name brand-name--light" x="186" y="252" font-size="19">vornex</text>
    <text class="tagline tagline--light" x="186" y="262" font-size="7">Clean Made Simple</text>
  </g>

  <!-- Narrow side panel -->
  <text class="brand-name brand-name--blue" x="500" y="128" font-size="18" text-anchor="middle">vornex</text>
  <g class="lockup" text-anchor="end">
    <text class="brand-name brand-name--blue" x="528" y="212" font-size="12">vornex</text>
    <text class="tagline tagline--blue" x="528" y="219" font-size="5">Clean Made Simple</text>
  </g>

  <!-- Front panel -->
  <polygon class="band" points="601,66 1126,68 1126,160 924,102 832,136 598,284"/>
  <polygon class="badge-dark" points="828,70 886,54 926,102 890,154 830,138"/>
  <g class="lockup" text-anchor="end">
    <text class="brand-name brand-name--light" x="912" y="107" font-size="16">vornex</text>
    <text class="tagline tagline--light" x="912" y="116" font-size="6">Clean Made Simple</text>
  </g>
  <g class="lockup" text-anchor="end">
    <text class="brand-name brand-name--light" x="682" y="203" font-size="12">vornex</text>
    <text class="tagline tagline--light" x="682" y="210" font-size="5">Clean Made Simple</text>
  </g>
  <text class="headline" x="780" y="221">LOREM IPSU-</text>
  <text class="headline" x="780" y="243">MOR SIT AMET,</text>

  <!-- Back panel -->
  <text class="brand-name brand-name--blue" x="1030" y="190" font-size="8" text-anchor="middle">vornex</text>
  <text class="body-copy" x="940" y="228">Lorem ipsum dolor sit amet, consectetur</text>
  <text class="body-copy" x="940" y="235">adipiscing elit. Donec ut aliquet mi. Sus-</text>
  <text class="body-copy" x="940" y="242">pendisse nulla odio, feugiat nec est eu,</text>
</svg>
</body>
</html>
```